Supplement Bottle Label Design and Creative Lifestyle Images

We are a medical home consumer brand and we are releasing a supplement line of products called "Velbrook Nutrition". We are in need of a supplement bottle design for our supplement line, Velbrook Nutrition. We are looking for a very appealing, simple, and clean design, but with a medical feel to it.

We would like to see designs with a black background as well as designs with a white background. Bottle size will approximately be 200cc and label will about be 7" x 2.5", but this size is subject to change.

We really like the Pirlen Nutrition design and the Gantry Lab, however, we like the medical style of Nutrition Keystones. Please reference the links below.

To start off, the title of this bottle will be "Calm-Spire". We will need all similar warning about FDA, made in USA, non-GMA, GMP, ect. Please use the formula below to start:

2 Pills per serving
Blueberry pterostilbene - 10mg
Bacopa - 150mg
Gingko Biloba - 50mg
Vinpocetine - 10mg
Alpha-GPC -150mg
TAU - 35mg

https://www.shopvarn.example/Pirlen-Nutrition/b/ref=bl_dp_s_web_48213907562?ie=UTF8&node=48213907562&field-lbr_brands_browse-bin=Pirlen+Nutrition

https://www.shopvarn.example/l/7394208156

https://www.shopvarn.example/Nutrition-Keystones/b/ref=bl_dp_s_web_86420531977?ie=UTF8&node=86420531977&field-lbr_brands_browse-bin=Nutrition+Keystones

Industry/Entity Type

Medical

```html
<!DOCTYPE html>
<html lang="en">
<head>
<meta charset="utf-8">
<title>Velbrook Nutrition – Calm Spire Label</title>
<link rel="stylesheet" href="https://fonts.googleapis.com/css2?family=Questrial&family=Josefin+Sans:wght@300&family=Oswald:wght@500&family=Montserrat:wght@500;600&display=swap">
<style>
  :root {
    --bg: #8c8c8c;
    --label-black: #151617;
    --label-dark: #222426;
    --brand-blue: #3aa8dd;
    --line-blue: #2b9ed8;
    --ribbon-blue: #3aa8dd;
    --ribbon-green: #6cbf3a;
    --ribbon-orange: #f0a043;
    --text-white: #f4f4f4;
    --text-dark: #1a1a1a;
    --badge-white: #f2f2f2;
    --badge-green: #5aa83a;
  }
  * { margin: 0; padding: 0; box-sizing: border-box; }
  html, body { width: 1200px; height: 1200px; overflow: hidden; }
  body {
    background: var(--bg);
    display: flex;
    align-items: center;
    justify-content: center;
  }
  .label {
    position: relative;
    width: 800px;
    height: 800px;
    background: linear-gradient(160deg, var(--label-dark) 0%, var(--label-black) 60%, #0e0f10 100%);
    color: var(--text-white);
    overflow: hidden;
  }
  .band {
    position: absolute;
    left: 0;
    width: 100%;
    background: var(--line-blue);
  }
  .band--top-thick { top: 18px; height: 8px; }
  .band--top-thin { top: 34px; height: 3px; }
  .band--bottom-thin { bottom: 38px; height: 3px; }
  .band--bottom-thick { bottom: 18px; height: 8px; }
  .brand-tab {
    position: absolute;
    top: 0;
    left: 240px;
    width: 320px;
    height: 150px;
    background: var(--brand-blue);
    border-radius: 0 0 6px 6px;
    display: flex;
    flex-direction: column;
    align-items: center;
    justify-content: center;
    font-family: "Questrial", sans-serif;
    font-size: 46px;
    line-height: 1.1;
    color: var(--text-white);
    text-align: center;
    padding-top: 14px;
  }
  .product-title {
    position: absolute;
    top: 185px;
    left: 0;
    width: 100%;
    text-align: center;
    font-family: "Josefin Sans", sans-serif;
    font-weight: 300;
    font-size: 118px;
    line-height: 118px;
    letter-spacing: -2px;
  }
  .product-subtitle {
    position: absolute;
    top: 420px;
    left: 0;
    width: 100%;
    text-align: center;
    font-family: "Oswald", sans-serif;
    font-weight: 500;
    font-size: 38px;
    line-height: 56px;
    letter-spacing: 0.5px;
  }
  .benefit-ribbons {
    position: absolute;
    top: 540px;
    left: 90px;
    width: 640px;
    height: 68px;
  }
  .benefit-ribbons text {
    font-family: "Montserrat", sans-serif;
    font-weight: 500;
    font-size: 28px;
  }
  .supplement-note {
    position: absolute;
    top: 672px;
    left: 150px;
    width: 400px;
    text-align: center;
    font-family: "Oswald", sans-serif;
    font-weight: 500;
    font-size: 26px;
    letter-spacing: 1px;
  }
  .capsule-count {
    position: absolute;
    top: 724px;
    left: 150px;
    width: 400px;
    text-align: center;
    font-family: "Montserrat", sans-serif;
    font-weight: 600;
    font-size: 24px;
  }
  .certifications {
    position: absolute;
    top: 668px;
    left: 568px;
    width: 210px;
    height: 76px;
  }
</style>
</head>
<body>
  <main class="label">
    <div class="band band--top-thick"></div>
    <div class="band band--top-thin"></div>

    <div class="brand-tab">
      <span>Velbrook</span>
      <span>Nutrition</span>
    </div>

    <h1 class="product-title">CALM<br>SPIRE</h1>

    <p class="product-subtitle">BRAIN PERFORMANCE<br>FOCUS FORMULA</p>

    <svg class="benefit-ribbons" viewBox="0 0 640 68" aria-label="Focus, Clarity, Memory">
      <polygon points="0,6 196,6 218,34 196,62 0,62 18,34" fill="var(--ribbon-blue)"/>
      <text x="106" y="44" text-anchor="middle" fill="var(--text-dark)">FOCUS*</text>
      <polygon points="206,6 410,6 432,34 410,62 206,62 228,34" fill="var(--ribbon-green)"/>
      <text x="320" y="44" text-anchor="middle" fill="var(--text-dark)">CLARITY*</text>
      <polygon points="420,2 618,2 640,30 618,58 420,58 442,30" fill="var(--ribbon-orange)"/>
      <text x="530" y="40" text-anchor="middle" fill="var(--text-dark)">MEMORY*</text>
    </svg>

    <p class="supplement-note">A DIETARY SUPPLEMENT</p>
    <p class="capsule-count">90 Capsules</p>

    <svg class="certifications" viewBox="0 0 210 76" role="img" aria-label="Certification badges">
      <circle cx="34" cy="42" r="32" fill="var(--badge-white)"/>
      <circle cx="34" cy="42" r="24" fill="none" stroke="var(--badge-green)" stroke-width="4"/>
      <circle cx="108" cy="38" r="32" fill="var(--badge-white)"/>
      <circle cx="108" cy="38" r="24" fill="none" stroke="var(--badge-green)" stroke-width="4"/>
      <circle cx="178" cy="32" r="30" fill="var(--badge-green)"/>
      <circle cx="178" cy="32" r="22" fill="var(--badge-white)"/>
    </svg>

    <div class="band band--bottom-thin"></div>
    <div class="band band--bottom-thick"></div>
  </main>
</body>
</html>
```